vermalo web design

- Company / Site Description
We are developing a website that will allow anyone in Europe to find in one click, cultural things to do (Exhibition, Museum, Monument, Zoo, Aquarium, Archaeological site…) with friends or family, and to organize the visit (book a ticket / a private visit, book a restaurant nearby…).

Examples
1. You're in London with your girlfriend, it's saturday 10 am, you have two hours to spend and you want to see an exhibition. We provide you in one click all the exhibition matching your location / time and date.

2. You're in Berlin with some friends, it's thursday night you want to go out, but you don't know what to do. We provide you a list of experience, you can select for instance "I want to be on top of the world", and we show you a list of venues matching the selected experience / date / time /location of your request.

- Brand name : Vermalo
- Activity : Cultural Leisure, cultural entertainment

- Target audience
Broad target will be between 20 and 55. Core target will be between 25 and 40. Most likely to live in a city and in Europe.

- Behaviours and preferences
Our user is under time constraint (few minutes to find and choose his visit), idea constraint (is not sure about what to do and see) and money constraint.
He wants to have an easy to use website, not cluttered with information, focussed on added value information. He wants to have a website which is modern, fun and elegant that he will deem as professional and trustworthy.

- Our expectations (Do’s and Don’t)
We want to move away from traditional design. We want some OUT OF THE BOX design. Think of a website design that will look like an app design.
We want to make an awesome / extra ordinary /remember-able design. The design must be so cool, that the user wants to come back to the site. In two words: THINK EXTRAORDINARY.
You can use photos to help the user understand functions. If you use photo, use creative commons license photo.
Avoid black colors

- Functional Requirements
We need Four pages:
1. Home Page (desktop and mobile version): it’s both the homepage and the assistant page. This page will allow the user to find in one click his visit (please refer to the pdf file Assistant home page). The page must be self-explanatory for a first time user.
2. Assistant result page (desktop version): it’s the page that display the results found by the assistant based on the criteria search (please refer to the pdf file mockup - Assistant result page)
3. Site / Event page (desktop version): it’s the page that display each result information (please refer to the pdf file mockup – Event / Site Page)
The pdf files list all the elements include in each page + gives you a mockup of each page (just to put in perspective the element required). You are completely free about the design.
We don’t have the logo yet. Use a dummy logo for your page design.
The selected winner can expect to work with us immediately after the contest and on a on a regular basis later on.

- Technical Requirements
No Flash
For the winner, we will manage the CSS you will just need to provide :
. One PSD file containing all the pages
. Inside the PSD file we want for each page two groups: the first group will embed the desktop design, the second group will embed the responsive mobile design (Home Page only).
In total there should be 4 groups inside the PSD file (3 desktop groups, 1 mobile group).
Each group must contain all the elements specified in the pdf file

Website we like
http://demo.plandorix.example/?theme=Velunt
http://rosabel.quintorhub.example/#home
http://blogsite.fenk.daltoroute.example/2/
http://demo.plandorix.example/?theme=Mosaru
http://www.quarnivo.example/themes/lumbe/
http://gridmarket.example/item/tav-responsive-photography-blog-theme/full_screen_preview/8146027
http://items.zkvortel.example/?product=example
http://uk.harnoway.example

Reason: Due to the request of several designers, we have agreed to add 7 additional days to the contest deadline. Thank you. The vermalo team

Reason: We still need to collect all the votes. Sorry for the delay.

Reason: Hello, We extend the contest deadline, in order to collect all the votes from the poll. We should have everything finalized by sunday. Thank you vermalo team

```html
<!DOCTYPE html>
<html lang="en">
<head>
<meta charset="utf-8">
<title>Vermalo – Assistant results</title>
<link href="https://fonts.googleapis.com/css2?family=Arimo:wght@400;700&display=swap" rel="stylesheet">
<style>
:root{
  --page-bg:#4876ad;
  --topbar:#cfdbea;
  --ink:#1b1b1b;
  --teal:#26b5b0;
  --panel:#111a25;
  --panel-head:#000000;
  --rank:#59616d;
  --search:#8e8e8e;
  --summary:#1c3150;
  --city:#4d4b8d;
  --date:#5b7a4b;
  --time:#3d7a5d;
  --mood:#3b7a80;
  --criteria:#1d2d45;
  --star:#e67e16;
  --white:#ffffff;
}
*{box-sizing:border-box;margin:0;padding:0}
html,body{width:1200px;height:800px;overflow:hidden}
body{position:relative;background:var(--page-bg);font-family:"Arimo",Arial,sans-serif;color:var(--white)}

.topbar{position:absolute;left:0;top:0;width:1200px;height:45px;background:var(--topbar);color:var(--ink)}
.brand{position:absolute;left:52px;top:9px;font-size:24px;letter-spacing:-0.5px}
.nav-link{position:absolute;top:13px;font-size:14px}
.nav-link.active{left:246px;height:32px;border-bottom:2px solid var(--teal);width:56px}
.nav-fav{left:375px}
.search{position:absolute;left:954px;top:13px;width:108px;height:18px;background:var(--search);font-size:11px;padding:3px 6px;color:#2a2a2a}
.search svg{position:absolute;right:6px;top:3px}
.login{position:absolute;left:1101px;top:15px;font-size:12px}
.user{position:absolute;left:1145px;top:12px;width:33px;height:18px;background:#9aa6b4}

.criteria{position:absolute;left:22px;top:65px;width:223px;height:390px}
.crit-row{height:63px;padding:0 16px;display:flex;align-items:flex-end;padding-bottom:7px;font-size:18px;border-bottom:1px solid rgba(0,0,0,.25)}
.summary{background:var(--summary);height:80px;display:block;padding:22px 16px 0}
.summary h2{font-size:18px;font-weight:400}
.summary p{font-size:13px;margin-top:2px}
.city{background:var(--city)}
.date{background:var(--date)}
.time{background:var(--time)}
.mood{background:var(--mood)}
.change{background:var(--criteria);height:57px;font-size:12px;padding:0 18px;display:flex;align-items:center;position:relative;overflow:hidden}
.change .reset{position:absolute;right:-14px;top:10px;width:36px;height:36px;border-radius:50%;background:#c9ccd0}

.map{position:absolute;left:22px;top:481px;width:223px;height:264px;background:linear-gradient(160deg,#e8e4da,#d9d5c8 60%,#cfd7c6);box-shadow:3px 4px 6px rgba(0,0,0,.35)}
.weather{position:absolute;right:0;bottom:0;width:80px;height:38px;background:rgba(91,168,180,.85);font-size:12px;padding:13px 10px}

.results{position:absolute;left:302px;width:880px;background:var(--panel)}
.sites{top:65px;height:415px}
.exhibitions{top:501px;height:244px}
.results-head{height:40px;background:var(--panel-head);position:relative}
.results-head .tab{position:absolute;left:0;bottom:0;width:48px;height:3px;background:var(--teal)}
.results-head h2{position:absolute;left:60px;top:11px;font-size:18px;font-weight:400}

.venue{position:absolute;left:0;width:880px;height:90px}
.rank{position:absolute;left:-30px;top:12px;width:60px;height:60px;border-radius:50%;background:var(--rank);font-size:13px;padding:21px 0 0 36px;clip-path:inset(0 0 0 30px)}
.thumb{position:absolute;left:49px;top:0;width:105px;height:89px}
.venue h3{position:absolute;left:182px;top:0;font-size:13px;font-weight:400}
.venue p{position:absolute;left:182px;top:21px;width:680px;font-size:11px;line-height:13px}
.meta{position:absolute;left:182px;top:65px;display:flex;align-items:center;font-size:9px}
.meta svg{margin-right:6px}
.meta span{margin-right:12px}

.more{position:absolute;left:404px;bottom:0;width:84px;height:42px;border-radius:42px 42px 0 0;background:var(--rank)}
.more svg{position:absolute;left:24px;top:18px}

.footer{position:absolute;left:22px;top:768px;width:1178px;height:32px;background:var(--white);color:var(--ink);font-size:11px}
.footer .lang{position:absolute;left:18px;top:12px}
.footer .plus{position:absolute;left:1098px;top:12px}
.footer .drop{position:absolute;left:1136px;top:0;width:20px;height:32px;background:#a7a7a7}
</style>
</head>
<body>

<header class="topbar">
  <div class="brand">Vermalo</div>
  <div class="nav-link active">Assistant</div>
  <div class="nav-link nav-fav">My Favourites</div>
  <div class="search">I SEARCH
    <svg width="11" height="11" viewBox="0 0 11 11"><circle cx="4.5" cy="4.5" r="3" fill="none" stroke="#fff" stroke-width="1.6"/><line x1="7" y1="7" x2="10" y2="10" stroke="#fff" stroke-width="1.8"/></svg>
  </div>
  <div class="login">LOGIN</div>
  <div class="user">
    <svg width="33" height="18" viewBox="0 0 33 18"><circle cx="9" cy="6" r="3.5" fill="#fff"/><path d="M3 17c0-5 12-5 12 0z" fill="#fff"/><path d="M22 7l4 4 4-4" fill="none" stroke="#fff" stroke-width="1.5"/></svg>
  </div>
</header>

<aside class="criteria">
  <div class="summary"><h2>6 Sites and 1 Exhibition</h2><p>Match your selection</p></div>
  <div class="crit-row city">PARIS</div>
  <div class="crit-row date">14 DEC</div>
  <div class="crit-row time">11:00</div>
  <div class="crit-row mood">MEET CELEBRITIES</div>
  <div class="change">CHANGE CRITERIA
    <div class="reset"><svg width="36" height="36" viewBox="0 0 36 36"><path d="M14 14a5 5 0 1 0 4-1" fill="none" stroke="#1d2d45" stroke-width="1.6"/></svg></div>
  </div>
</aside>

<div class="map" role="img" aria-label="Street map of Paris with pins marking the matching venues">
  <div class="weather">16°c
    <svg width="22" height="14" viewBox="0 0 22 14" style="vertical-align:-3px"><path d="M5 13h13a4 4 0 0 0 0-8 5 5 0 0 0-9-1 4 4 0 0 0-4 9z" fill="none" stroke="#fff" stroke-width="1.3"/></svg>
  </div>
</div>

<section class="results sites">
  <div class="results-head"><span class="tab"></span><h2>SITES</h2></div>

  <article class="venue" style="top:57px">
    <div class="rank">1.</div>
    <div class="thumb" role="img" aria-label="Red facade of the wax museum" style="background:linear-gradient(160deg,#c96a5e,#9c3b33 60%,#b98a76)"></div>
    <h3>Musée Valorin</h3>
    <p>Jujubes jelly beans pastry cake biscuit jujubes cheesecake. Chocolate bar chocolate bar topping lemon drops tootsie roll. Macaroon chocolate bar sweet tart powder tootsie roll macaroon liquorice.</p>
    <div class="meta">
      <svg width="22" height="22" viewBox="0 0 22 22"><path d="M11 1l3 7h7l-6 5 2 8-6-4-6 4 2-8-6-5h7z" fill="var(--star)"/></svg>
      <span>Paris – 16 km</span>
      <svg width="16" height="16" viewBox="0 0 16 16"><circle cx="8" cy="8" r="7" fill="none" stroke="#fff" stroke-width="1.2"/><path d="M8 3v5l-2 3" fill="none" stroke="#fff" stroke-width="1.2"/></svg>
      <span>close in 8h</span>
      <span>GET DIRECTIONS</span>
    </div>
  </article>

  <article class="venue" style="top:167px">
    <div class="rank">2.</div>
    <div class="thumb" role="img" aria-label="Stone townhouse facade under a blue sky" style="background:linear-gradient(180deg,#7fa6d6,#a49a8e 45%,#6b6058)"></div>
    <h3>Maison de Léandre…</h3>
    <p>Jujubes jelly beans pastry cake biscuit jujubes cheesecake. Chocolate bar chocolate bar topping lemon drops tootsie roll. Macaroon chocolate bar sweet tart powder tootsie roll macaroon liquorice.</p>
    <div class="meta">
      <svg width="22" height="22" viewBox="0 0 22 22"><path d="M11 1l3 7h7l-6 5 2 8-6-4-6 4 2-8-6-5h7z" fill="var(--star)"/></svg>
      <span>Paris – 16 km</span>
      <svg width="16" height="16" viewBox="0 0 16 16"><circle cx="8" cy="8" r="7" fill="none" stroke="#fff" stroke-width="1.2"/><path d="M8 3v5l-2 3" fill="none" stroke="#fff" stroke-width="1.2"/></svg>
      <span>close in 8h</span>
      <span>GET DIRECTIONS</span>
    </div>
  </article>

  <article class="venue" style="top:277px">
    <div class="rank">3.</div>
    <div class="thumb" role="img" aria-label="Modern cinema building with trees" style="background:linear-gradient(170deg,#4f8ad0,#d9d6cc 50%,#5f7a3c)"></div>
    <h3>Cinéscope Orsel</h3>
    <p>Jujubes jelly beans pastry cake biscuit jujubes cheesecake. Chocolate bar chocolate bar topping lemon drops tootsie roll. Macaroon chocolate bar sweet tart powder tootsie roll macaroon liquorice.</p>
    <div class="meta">
      <svg width="22" height="22" viewBox="0 0 22 22"><path d="M11 1l3 7h7l-6 5 2 8-6-4-6 4 2-8-6-5h7z" fill="var(--star)"/></svg>
      <span>Paris – 16 km</span>
      <svg width="16" height="16" viewBox="0 0 16 16"><circle cx="8" cy="8" r="7" fill="none" stroke="#fff" stroke-width="1.2"/><path d="M8 3v5l-2 3" fill="none" stroke="#fff" stroke-width="1.2"/></svg>
      <span>close in 8h</span>
      <span>GET DIRECTIONS</span>
    </div>
  </article>

  <div class="more"><svg width="36" height="16" viewBox="0 0 36 16"><path d="M2 2l16 12 16-12" fill="none" stroke="#fff" stroke-width="2"/></svg></div>
</section>

<section class="results exhibitions">
  <div class="results-head"><span class="tab"></span><h2>EXHIBITIONS</h2></div>

  <article class="venue" style="top:58px">
    <div class="rank">1.</div>
    <div class="thumb" role="img" aria-label="Exhibition poster with a line drawing" style="background:linear-gradient(135deg,#fafafa,#efece6)"></div>
    <h3>Jules Marvande …</h3>
    <p>Jujubes jelly beans pastry cake biscuit jujubes cheesecake. Chocolate bar chocolate bar topping lemon drops tootsie roll. Macaroon chocolate bar sweet tart powder tootsie roll macaroon liquorice.</p>
    <div class="meta">
      <svg width="22" height="22" viewBox="0 0 22 22"><path d="M11 1l3 7h7l-6 5 2 8-6-4-6 4 2-8-6-5h7z" fill="var(--star)"/></svg>
      <span>Paris – 16 km</span>
      <svg width="16" height="16" viewBox="0 0 16 16"><circle cx="8" cy="8" r="7" fill="none" stroke="#fff" stroke-width="1.2"/><path d="M8 3v5l-2 3" fill="none" stroke="#fff" stroke-width="1.2"/></svg>
      <span>close in 8h</span>
      <span>GET DIRECTIONS</span>
    </div>
  </article>
</section>

<footer class="footer">
  <span class="lang">LANGUAGE &gt; EN</span>
  <span class="plus">PLUS</span>
  <span class="drop"><svg width="20" height="32" viewBox="0 0 20 32"><path d="M6 14l4 4 4-4" fill="none" stroke="#fff" stroke-width="1.5"/></svg></span>
</footer>

</body>
</html>
```